Cedarline Residences —-

Letter head for my apartment building of 15 Floors
In Tessoro, Valmora

CEDARLINE RESIDENCIES
14 KIVARA RIDGE ROAD
LUMARA HEIGHTS - TESSORO
P.O. BOX 38516
KAMPALA— UGANDA

```html
<!DOCTYPE html>
<html lang="en">
<head>
<meta charset="utf-8">
<title>Cedarline Residences — Letterhead</title>
<link href="https://fonts.googleapis.com/css2?family=Lato:wght@400;700&display=swap" rel="stylesheet">
<style>
  :root {
    --backdrop: #cdc3c1;
    --paper: #fdfdfb;
    --navy: #1b1f5c;
    --ink: #3a3a44;
    --rule: #9a9a9a;
    --footer-text: #5c5c62;
  }
  * { margin: 0; padding: 0; box-sizing: border-box; }
  html, body {
    width: 1200px;
    height: 784px;
    overflow: hidden;
    background: var(--backdrop);
    font-family: "Lato", sans-serif;
  }
  .letterhead {
    position: absolute;
    left: 340px;
    top: 22px;
    width: 520px;
    height: 740px;
    background: var(--paper);
    box-shadow: 0 6px 18px rgba(60, 40, 40, 0.18);
  }
  .brand {
    position: absolute;
    left: 44px;
    top: 46px;
    display: flex;
    align-items: center;
    gap: 8px;
    color: var(--navy);
    font-weight: 700;
    font-size: 15px;
    letter-spacing: 1.6px;
    text-transform: uppercase;
  }
  .brand-square {
    width: 12px;
    height: 12px;
    background: var(--navy);
  }
  .contact {
    position: absolute;
    right: 30px;
    top: 40px;
    padding-left: 12px;
    border-left: 1px solid var(--ink);
    color: var(--ink);
    font-size: 8.5px;
    font-style: normal;
    line-height: 1.4;
    white-space: nowrap;
  }
  .contact-address { margin-bottom: 4px; }
  .contact-line {
    display: flex;
    align-items: center;
    gap: 5px;
  }
  .contact-line svg {
    width: 8px;
    height: 8px;
    flex: none;
  }
  .footer-rule {
    position: absolute;
    left: 0;
    right: 0;
    bottom: 26px;
    display: flex;
    align-items: center;
    gap: 14px;
  }
  .footer-rule::before,
  .footer-rule::after {
    content: "";
    flex: 1;
    height: 1px;
    background: var(--rule);
  }
  .footer-name {
    color: var(--footer-text);
    font-size: 10px;
    letter-spacing: 2.6px;
    text-transform: uppercase;
  }
  .footer-band {
    position: absolute;
    left: 0;
    right: 0;
    bottom: 0;
    height: 11px;
    background: var(--navy);
  }
</style>
</head>
<body>
  <main class="letterhead">
    <header class="brand">
      <span class="brand-square"></span>
      <span class="brand-name">Cedarline Residences</span>
    </header>

    <address class="contact">
      <div class="contact-address">
        14 Kivara Ridge Road<br>
        Lumara Heights - Tessoro<br>
        P.O. Box 38516<br>
        Tessoro, Valmora
      </div>
      <div class="contact-line">
        <svg viewBox="0 0 10 10" aria-hidden="true"><path d="M2 1 L4 1 L4.6 3.2 L3.4 4 Q4.4 5.8 6 6.6 L6.8 5.4 L9 6 L9 8 Q5 9.4 1.2 4.2 Q0.6 2.2 2 1 Z" fill="var(--navy)"/></svg>
        (256) 414-2087
      </div>
      <div class="contact-line">
        <svg viewBox="0 0 10 10" aria-hidden="true"><rect x="0.8" y="2" width="8.4" height="6" fill="var(--navy)"/><path d="M0.8 2 L5 5.4 L9.2 2" fill="none" stroke="var(--paper)" stroke-width="0.9"/></svg>
        info@cedarlineres.ug
      </div>
      <div class="contact-line">
        <svg viewBox="0 0 10 10" aria-hidden="true"><circle cx="5" cy="5" r="4" fill="none" stroke="var(--navy)" stroke-width="1"/><ellipse cx="5" cy="5" rx="1.7" ry="4" fill="none" stroke="var(--navy)" stroke-width="0.8"/><path d="M1 5 H9" stroke="var(--navy)" stroke-width="0.8"/></svg>
        www.cedarlineres.ug
      </div>
    </address>

    <footer>
      <div class="footer-rule">
        <span class="footer-name">Cedarline Residencies LLC</span>
      </div>
      <div class="footer-band"></div>
    </footer>
  </main>
</body>
</html>
```